Flaschenetiketten-Design in rechteckiger Grundform für Biermanufaktur
Der Kontakt war sehr professionell und angenehm. Wir wurden hilfreich beraten. Auf unser Feedback haben wir in kurzer Zeit jeweils neue Entwürfe erhalten. Die Zusammenarbeit und der Service war deutlich über unseren Vorstellungen. Wir können QuendraMill nur weiterempfehlen!
Zielgruppe
Wir repräsentieren eine Bier-Manufaktur in der Gründungsphase und sind auf der Suche nach einem Designvorschlag für die Flaschenetiketten.
Unsere Zielgruppe sind Liebhaber, die auf der Suche nach dem Speziellen und Lokalen sind. Der Biergenuss abseits des Massenmarktes soll im Entwurf sichtbar/transportiert werden. Die Bier-Manufaktur steht zeitgleich für Trend-Kreationen mit bodenständigem Ursprung.
Aufgabenstellung
Die Herkunft der Gründer Familie aus dem Schweizer Kanton Simplon soll im Vordergrund stehen, hierzu bitte das Familienwappen / einzelne Elemente siehe Dateiupload berücksichtigen.
Das Etikett soll eine rechteckige Grundform haben.
Folgende Angaben sollen sich im Etikett wiederfinden:
- Biersorte: 'Lager' (zukünftig soll es möglich sein, Biersorte auf dem Etikett zu wechseln)
Brand: 'Merry Marwen'
'Biermanufaktur Walliser Ursprungs'
Die Schrift soll klar und nicht zu verspielt sein.

```html
<!DOCTYPE html>
<html lang="de">
<head>
<meta charset="utf-8">
<title>Merry Marwen – Lagerbier Etikett</title>
<link rel="stylesheet" href="https://fonts.googleapis.com/css2?family=Josefin+Sans:wght@500;600;700&display=swap">
<style>
  :root {
    --page-bg: #ffffff;
    --label-bg: #ffffff;
    --frame-blue: #5b87cb;
    --crest-blue: #5683c9;
    --crest-line: #2b2b2b;
    --watermark-grey: #e4e4e4;
    --forest-green: #2f5230;
    --ink: #111111;
  }
  * { box-sizing: border-box; margin: 0; padding: 0; }
  html, body {
    width: 844px;
    height: 1200px;
    overflow: hidden;
    background: var(--page-bg);
  }
  .canvas {
    position: relative;
    width: 844px;
    height: 1200px;
  }
  .label {
    position: absolute;
    left: 62px;
    top: 201px;
    width: 720px;
    height: 797px;
    background: var(--label-bg);
    border: 13px solid var(--frame-blue);
    box-shadow: 6px 10px 18px rgba(0, 0, 0, 0.35);
    overflow: hidden;
    font-family: "Josefin Sans", sans-serif;
  }
  .label__backdrop {
    position: absolute;
    inset: 0;
    width: 100%;
    height: 100%;
  }
  .label__crest {
    position: absolute;
    left: 212px;
    top: 49px;
    width: 267px;
    height: 326px;
    background: var(--crest-blue);
    border: 3px solid var(--crest-line);
    border-radius: 4px 4px 40px 40px;
  }
  .label__variety {
    position: absolute;
    left: 0;
    right: 0;
    top: 388px;
    text-align: center;
    color: var(--forest-green);
    font-weight: 600;
    font-size: 31px;
    letter-spacing: 3px;
    word-spacing: 6px;
  }
  .label__brand {
    position: absolute;
    left: 0;
    right: 0;
    top: 474px;
    text-align: center;
    color: var(--ink);
    font-weight: 700;
    font-size: 108px;
    line-height: 104px;
    letter-spacing: 5px;
  }
  .label__brand span { display: block; }
  .label__tagline {
    position: absolute;
    left: 0;
    right: 0;
    top: 697px;
    text-align: center;
    color: var(--forest-green);
    font-weight: 600;
    font-size: 21px;
    letter-spacing: 3.2px;
  }
</style>
</head>
<body>
  <main class="canvas">
    <section class="label">
      <svg class="label__backdrop" viewBox="0 0 694 771" role="img" aria-label="Faint enlarged family crest as background decoration">
        <g transform="rotate(-18 360 420)">
          <rect x="70" y="120" width="520" height="640" rx="50" fill="var(--watermark-grey)"/>
        </g>
      </svg>
      <div class="label__crest" role="img" aria-label="Family coat of arms: stars, cross on orb and green hills on blue shield"></div>
      <p class="label__variety">- LAGERBIER -</p>
      <h1 class="label__brand"><span>MERRY</span><span>MARWEN</span></h1>
      <p class="label__tagline">BIERMANUFAKTUR WALLISER URSPRUNGS</p>
    </section>
  </main>
</body>
</html>
```